RK Bastone Construction Inc.

Design a new business card for our construction company
To be removed from current card:
Delete 25 years
Delete Tenant fit up Renovations section

```html
<!DOCTYPE html>
<html lang="en">
<head>
<meta charset="utf-8">
<title>RK Bastone Construction Inc. – Business Card</title>
<link rel="stylesheet" href="https://fonts.googleapis.com/css2?family=Krona+One&family=Barlow:wght@500&family=Montserrat:wght@500;600&display=swap">
<style>
  :root {
    --backdrop: #8c8d90;
    --brand-purple: #553174;
    --card-white: #ffffff;
    --ink: #111111;
    --divider: #b9b9bd;
  }
  html, body {
    margin: 0;
    padding: 0;
    width: 1200px;
    height: 1200px;
    overflow: hidden;
  }
  body {
    position: relative;
    background: var(--backdrop);
  }
  .card {
    position: absolute;
    width: 696px;
    height: 408px;
  }
  /* Front */
  .card-front {
    left: 246px;
    top: 157px;
    background: var(--brand-purple);
    color: var(--card-white);
  }
  .front-wordmark {
    position: absolute;
    left: 0;
    right: 0;
    top: 148px;
    text-align: center;
    font-family: "Krona One", sans-serif;
    color: var(--card-white);
    line-height: 1;
  }
  .front-wordmark .wordmark-name {
    display: block;
    font-size: 38px;
    letter-spacing: 0.5px;
  }
  .front-wordmark .wordmark-sub {
    display: block;
    margin-top: 10px;
    font-size: 21px;
    letter-spacing: 1px;
  }
  .front-web {
    position: absolute;
    left: 0;
    right: 0;
    top: 512px;
    top: 354px;
    text-align: center;
    font-family: "Montserrat", sans-serif;
    font-weight: 500;
    font-size: 16px;
    letter-spacing: 3.4px;
  }
  /* Back */
  .card-back {
    left: 241px;
    top: 619px;
    background: var(--card-white);
    color: var(--ink);
  }
  .back-wordmark {
    position: absolute;
    left: 34px;
    top: 168px;
    width: 300px;
    font-family: "Krona One", sans-serif;
    color: var(--brand-purple);
    line-height: 1;
  }
  .back-wordmark .wordmark-name {
    display: block;
    font-size: 25px;
  }
  .back-wordmark .wordmark-sub {
    display: block;
    margin-top: 6px;
    font-size: 13.5px;
    letter-spacing: 1px;
  }
  .back-divider {
    position: absolute;
    left: 353px;
    top: 77px;
    width: 1px;
    height: 252px;
    background: var(--divider);
  }
  .contact-block {
    position: absolute;
    left: 383px;
    top: 0;
    right: 0;
  }
  .person-name {
    position: absolute;
    top: 90px;
    margin: 0;
    font-family: "Krona One", sans-serif;
    font-weight: 400;
    font-size: 18px;
    letter-spacing: 1.4px;
    white-space: nowrap;
  }
  .person-role {
    position: absolute;
    top: 123px;
    margin: 0;
    font-family: "Montserrat", sans-serif;
    font-weight: 600;
    font-size: 14px;
    letter-spacing: 4px;
  }
  .address {
    position: absolute;
    top: 168px;
    left: 6px;
    margin: 0;
    font-family: "Barlow", sans-serif;
    font-weight: 500;
    font-style: normal;
    font-size: 16px;
    line-height: 31px;
    white-space: nowrap;
  }
  .contact-list {
    position: absolute;
    top: 240px;
    left: 6px;
    margin: 0;
    padding: 0;
    list-style: none;
    font-family: "Barlow", sans-serif;
    font-weight: 500;
    font-size: 16px;
  }
  .contact-list li {
    display: flex;
    align-items: center;
    height: 30.5px;
    white-space: nowrap;
  }
  .contact-list svg {
    width: 14px;
    height: 14px;
    margin-right: 8px;
    fill: var(--brand-purple);
  }
</style>
</head>
<body>

<section class="card card-front" aria-label="Business card front">
  <div class="front-wordmark">
    <span class="wordmark-name">RK BASTONE</span>
    <span class="wordmark-sub">CONSTRUCTION INC</span>
  </div>
  <div class="front-web">www.rkbastoneconstruction.ca</div>
</section>

<section class="card card-back" aria-label="Business card back">
  <div class="back-wordmark">
    <span class="wordmark-name">RK BASTONE</span>
    <span class="wordmark-sub">CONSTRUCTION INC.</span>
  </div>
  <div class="back-divider"></div>
  <div class="contact-block">
    <h1 class="person-name">DARIO BASTONE</h1>
    <p class="person-role">MANAGER</p>
    <address class="address">2817 Hollins Rd.,<br>Suite 100, Ottawa, ON K1B4T7</address>
    <ul class="contact-list">
      <li>
        <svg viewBox="0 0 16 16" aria-hidden="true"><path d="M1 6c0-2 3-4 7-4s7 2 7 4v1h-3.5V5.5c-1-.6-2.2-.8-3.5-.8s-2.5.2-3.5.8V7H1z M3.5 8.5h9l1.5 5H2z M8 9.6a1.8 1.8 0 1 0 0 3.6a1.8 1.8 0 1 0 0-3.6z"/></svg>
        613-555-0142 ext. 221
      </li>
      <li>
        <svg viewBox="0 0 16 16" aria-hidden="true"><path d="M4.5 1h7a1 1 0 0 1 1 1v12a1 1 0 0 1-1 1h-7a1 1 0 0 1-1-1V2a1 1 0 0 1 1-1zm.6 1.8v9.4h5.8V2.8z"/></svg>
        613-555-0187
      </li>
      <li>
        <svg viewBox="0 0 16 16" aria-hidden="true"><path d="M1 3.5h14v9H1z M1.8 4.2L8 9l6.2-4.8" stroke="#fff" stroke-width="0.9"/></svg>
        dario@rkbastoneconst.ca
      </li>
    </ul>
  </div>
</section>

</body>
</html>
```